R&t Subterra

We specialize in CIPP pipe lining but do other underground utilities trenchless as well.

Target Market(s)

Trenchless sewer replacement

Contact Information for Business Card

Gavin Holtby 715-482-6130 Millbrook falls, wi

```html
<!DOCTYPE html>
<html lang="en">
<head>
<meta charset="utf-8">
<title>R&amp;t Subterra — Business Card</title>
<link rel="stylesheet" href="https://fonts.googleapis.com/css2?family=Poppins:wght@300;400;600&display=swap">
<style>
  :root {
    --stage: #222222;
    --card: #ffffff;
    --brand-blue: #2b8fcd;
    --brand-blue-deep: #2278b0;
    --ink: #1d1d1d;
    --grey: #9a9a9a;
  }
  * { box-sizing: border-box; margin: 0; padding: 0; }
  html, body {
    width: 1200px; height: 780px; overflow: hidden;
    background: var(--stage);
    font-family: "Poppins", sans-serif;
  }
  .stage { position: relative; width: 1200px; height: 780px; }

  .card {
    position: absolute;
    background: var(--card);
    border-radius: 22px;
    overflow: hidden;
    box-shadow: 0 14px 30px rgba(0,0,0,.45);
  }

  /* Front: portrait card */
  .card--front { left: 170px; top: 118px; width: 310px; height: 544px; }
  .brand {
    position: absolute;
    display: flex; align-items: center; gap: 8px;
    color: var(--brand-blue);
    font-weight: 600;
    white-space: nowrap;
  }
  .brand__dot {
    border-radius: 50%;
    background: var(--brand-blue);
    flex: none;
  }
  .card--front .brand { top: 34px; right: 30px; font-size: 21px; }
  .card--front .brand__dot { width: 18px; height: 18px; }

  .holder {
    position: absolute; left: 0; top: 100px;
    padding-left: 28px;
  }
  .holder::before {
    content: ""; position: absolute; left: 0; top: 4px;
    width: 12px; height: 34px; background: var(--brand-blue);
  }
  .holder__name { font-size: 27px; line-height: 1.3; }
  .holder__first { color: var(--brand-blue); font-weight: 600; }
  .holder__last { color: var(--grey); font-weight: 300; }
  .holder__role { font-size: 15px; color: var(--ink); margin-top: 2px; }

  .contact {
    position: absolute; left: 28px; top: 206px;
    list-style: none; font-size: 15px; color: var(--ink);
  }
  .contact li { display: flex; align-items: center; gap: 9px; margin-bottom: 8px; }
  .contact svg { width: 15px; height: 15px; flex: none; }

  .front-art {
    position: absolute; left: 0; bottom: 0;
    width: 310px; height: 290px; display: block;
  }

  /* Back: landscape card */
  .card--back {
    left: 560px; top: 236px; width: 544px; height: 310px;
    display: flex; align-items: center; justify-content: center;
  }
  .card--back .brand { position: static; font-size: 40px; gap: 14px; }
  .card--back .brand__dot { width: 34px; height: 34px; }
</style>
</head>
<body>
<main class="stage">

  <section class="card card--front" aria-label="Business card front">
    <div class="brand"><span class="brand__dot"></span>R&amp;t Subterra</div>

    <div class="holder">
      <p class="holder__name"><span class="holder__first">Gavin</span> <span class="holder__last">Holtby</span></p>
      <p class="holder__role">Founder &amp; CEO</p>
    </div>

    <ul class="contact">
      <li>
        <svg viewBox="0 0 24 24" aria-hidden="true"><path fill="var(--brand-blue)" d="M6.6 10.8a15 15 0 0 0 6.6 6.6l2.2-2.2a1 1 0 0 1 1-.25 11.4 11.4 0 0 0 3.6.57 1 1 0 0 1 1 1V20a1 1 0 0 1-1 1A17 17 0 0 1 3 4a1 1 0 0 1 1-1h3.5a1 1 0 0 1 1 1c0 1.25.2 2.45.57 3.57a1 1 0 0 1-.25 1z"/></svg>
        715-482-6130
      </li>
      <li>
        <svg viewBox="0 0 24 24" aria-hidden="true"><path fill="var(--brand-blue)" d="M12 2a7 7 0 0 0-7 7c0 5.2 7 13 7 13s7-7.8 7-13a7 7 0 0 0-7-7zm0 9.5A2.5 2.5 0 1 1 12 6.5a2.5 2.5 0 0 1 0 5z"/></svg>
        Millbrook falls, wi
      </li>
    </ul>

    <svg class="front-art" viewBox="0 0 310 290" role="img" aria-label="Large brand decoration in blue">
      <defs>
        <linearGradient id="artFill" x1="0" y1="0" x2="1" y2="1">
          <stop offset="0" stop-color="var(--brand-blue)"/>
          <stop offset="1" stop-color="var(--brand-blue-deep)"/>
        </linearGradient>
      </defs>
      <path d="M0 170 C 70 60, 200 10, 310 0 L310 290 L0 290 Z" fill="url(#artFill)"/>
    </svg>
  </section>

  <section class="card card--back" aria-label="Business card back">
    <div class="brand"><span class="brand__dot"></span>R&amp;t Subterra</div>
  </section>

</main>
</body>
</html>
```